Orrowind Partners Business Card

Looking for a design for our business cards. Need to look corporate and outstanding. I have enclosed our logos for the company. Orrowind partners is an investment firm for high level clients looking for advisory in their investments. White background or black is good. We will like to double sided options maybe at the back with just the logo of the firm.

Example of the info for the business card:

Edric Salvo
Managing Director

Panama Phone +507 384 7165
Switzerland Phone +41 44 917 2638
mail@orrowind-partners.example
www.orrowind-partners.example

Industry/Entity Type

Investment

```html
<!DOCTYPE html>
<html lang="en">
<head>
<meta charset="utf-8">
<title>Orrowind Partners Business Card</title>
<link rel="stylesheet" href="https://fonts.googleapis.com/css2?family=Source+Sans+3:wght@400;600;700&display=swap">
<style>
  :root {
    --backdrop: #d9d6d2;
    --card-black: #151515;
    --emboss: #4a4a4a;
    --white: #f4f4f4;
    --gold: #c99a2e;
    --muted: #8a8a8a;
    --contact: #d6d6d6;
  }
  * { box-sizing: border-box; margin: 0; padding: 0; }
  html, body {
    width: 1200px; height: 809px; overflow: hidden;
    background: var(--backdrop);
    font-family: "Source Sans 3", Arial, sans-serif;
  }
  .canvas {
    position: relative; width: 1200px; height: 809px;
    display: flex; align-items: center; justify-content: center; gap: 60px;
  }
  .card {
    position: relative; width: 510px; height: 291px;
    background: var(--card-black);
    border-radius: 6px;
    box-shadow: 0 10px 30px rgba(0,0,0,.25);
    overflow: hidden;
  }
  /* Front: name-only brand side */
  .card--front { display: flex; align-items: center; justify-content: center; }
  .wordmark {
    display: flex; align-items: center; gap: 14px;
    font-weight: 600; letter-spacing: .12em; text-transform: uppercase;
  }
  .wordmark__square { width: 22px; height: 22px; flex: none; }
  .card--front .wordmark { color: var(--emboss); font-size: 30px; }
  .card--front .wordmark__square { background: var(--emboss); }
  /* Back: details side */
  .card--back .wordmark {
    position: absolute; left: 36px; top: 108px;
    color: var(--white); font-size: 20px; gap: 12px; line-height: 1.15;
  }
  .wordmark__lines span { display: block; }
  .card--back .wordmark__square { background: var(--white); width: 18px; height: 18px; }
  .divider {
    position: absolute; left: 228px; top: 70px; width: 1px; height: 112px;
    background: linear-gradient(to bottom, transparent, var(--gold), transparent);
  }
  .person { position: absolute; left: 246px; top: 80px; }
  .person__name { color: var(--gold); font-weight: 700; font-size: 22px; line-height: 1.1; }
  .person__title { color: var(--muted); font-size: 13px; }
  .contacts {
    position: absolute; left: 246px; top: 168px; list-style: none;
    color: var(--contact); font-size: 13px; line-height: 21px;
  }
  .contacts li { display: flex; align-items: center; gap: 8px; white-space: nowrap; }
  .contacts svg { width: 11px; height: 11px; fill: var(--gold); flex: none; }
</style>
</head>
<body>
<main class="canvas">
  <section class="card card--front" aria-label="Card front">
    <div class="wordmark"><span class="wordmark__square"></span><span>Orrowind Partners</span></div>
  </section>

  <section class="card card--back" aria-label="Card back">
    <div class="wordmark"><span class="wordmark__square"></span><span class="wordmark__lines"><span>Orrowind</span><span>Partners</span></span></div>
    <div class="divider"></div>
    <div class="person">
      <p class="person__name">Edric Salvo</p>
      <p class="person__title">Managing Director</p>
    </div>
    <ul class="contacts">
      <li><svg viewBox="0 0 24 24"><path d="M6.6 10.8a15 15 0 0 0 6.6 6.6l2.2-2.2c.3-.3.7-.4 1-.2 1.1.4 2.3.6 3.6.6.6 0 1 .4 1 1V20c0 .6-.4 1-1 1A17 17 0 0 1 3 4c0-.6.4-1 1-1h3.5c.6 0 1 .4 1 1 0 1.3.2 2.5.6 3.6.1.3 0 .7-.2 1z"/></svg>+507 384 7165 (Panama)</li>
      <li><svg viewBox="0 0 24 24"><path d="M6.6 10.8a15 15 0 0 0 6.6 6.6l2.2-2.2c.3-.3.7-.4 1-.2 1.1.4 2.3.6 3.6.6.6 0 1 .4 1 1V20c0 .6-.4 1-1 1A17 17 0 0 1 3 4c0-.6.4-1 1-1h3.5c.6 0 1 .4 1 1 0 1.3.2 2.5.6 3.6.1.3 0 .7-.2 1z"/></svg>+41 44 917 2638 (Switzerland)</li>
      <li><svg viewBox="0 0 24 24"><path d="M2 5h20L12 13z M2 7l10 8 10-8v12H2z"/></svg>mail@orrowind-partners.example</li>
      <li><svg viewBox="0 0 24 24"><path d="M12 2a10 10 0 1 0 0 20 10 10 0 0 0 0-20zm6.9 6h-3a15 15 0 0 0-1.3-3.9A8 8 0 0 1 18.9 8zM12 4c.8 1.2 1.5 2.5 1.9 4h-3.8c.4-1.5 1.1-2.8 1.9-4zM4.3 14a8 8 0 0 1 0-4h3.4a16 16 0 0 0 0 4zm.8 2h3a15 15 0 0 0 1.3 3.9A8 8 0 0 1 5.1 16zm3-8h-3a8 8 0 0 1 4.3-3.9A15 15 0 0 0 8.1 8zM12 20c-.8-1.2-1.5-2.5-1.9-4h3.8c-.4 1.5-1.1 2.8-1.9 4zm2.3-6H9.7a14 14 0 0 1 0-4h4.6a14 14 0 0 1 0 4zm.3 5.9a15 15 0 0 0 1.3-3.9h3a8 8 0 0 1-4.3 3.9zM16.3 14a16 16 0 0 0 0-4h3.4a8 8 0 0 1 0 4z"/></svg>www.orrowind-partners.example</li>
    </ul>
  </section>
</main>
</body>
</html>
```